Flyer Design Project

We are a mortgage company Tamberlyn Funding Corp. that will be looking to mail out these flyers to promote Reverse Mortgages. Some clip art of Seniors (Happy Smile having a good time) Our phone number on the flyer in a few places 877-520-6184
Text: No Celebrity Endorsers or talking heads here
Solutions for seniors... Stop worrying Start Living
Say Goodby to monthly payments with a reverse mortgage
The Loan That Pays You
Secure Your Retirement With A Reverse Mortgage
GKP Goverment Insured
Retain Complete ownership of your Home
Save and Effective Financial Tool
Pay Off Credit cards Elimanate Mortgage payments improve your home or lifestyle
No Credit score or income requirements
Faceing a foreclosure a reverse mortgage can help
Is a reverse mortgage right for you? Get the facts from a qualified reverse mortgage originator
The text above does not have to be in that order
I am having trouble with my Logo so i am getting a new file and will be able to upload it to the flyer shortly just leave room for it
Seniors over the age of 62
Financial

```html
<!DOCTYPE html>
<html lang="en">
<head>
<meta charset="utf-8">
<title>Tamberlyn Funding Corp. – Reverse Mortgage Flyer</title>
<link href="https://fonts.googleapis.com/css2?family=Roboto+Condensed:wght@700&family=Source+Sans+3:wght@400;600&display=swap" rel="stylesheet">
<style>
  :root {
    --page-bg: #e6e6e6;
    --paper: #ffffff;
    --cyan: #1aaee0;
    --navy-blue: #2f6e96;
    --headline-blue: #2e6f99;
    --tick-red: #d0202a;
    --ink: #222222;
    --photo-warm: #d9a66a;
    --photo-mid: #c48a55;
    --photo-green: #7d8450;
  }
  * { box-sizing: border-box; margin: 0; padding: 0; }
  html, body { width: 830px; height: 1200px; overflow: hidden; }
  body { background: var(--page-bg); font-family: "Source Sans 3", Arial, sans-serif; }

  .flyer {
    position: absolute; left: 15px; top: 35px;
    width: 800px; height: 1130px;
    background: var(--paper);
    overflow: hidden;
    box-shadow: 0 6px 18px rgba(0,0,0,.25);
  }
  .abs { position: absolute; }

  .photo {
    left: 0; top: 0; width: 800px; height: 535px;
    background: linear-gradient(115deg, var(--photo-warm) 0%, var(--photo-mid) 40%, #a99766 70%, var(--photo-green) 100%);
  }
  .logo-box {
    left: 0; top: 0; width: 244px; height: 160px;
    background: var(--cyan);
    display: flex; align-items: center; justify-content: center; gap: 10px;
    padding: 0 14px;
  }
  .logo-mark { width: 18px; height: 18px; border-radius: 50%; background: #ffffff; flex: none; }
  .logo-name {
    font-family: "Roboto Condensed", Arial, sans-serif; font-weight: 700;
    color: #ffffff; font-size: 22px; line-height: 1.1;
  }
  .zigzag { left: 0; width: 800px; }

  .values-box {
    left: 425px; top: 451px; width: 375px; height: 242px;
    background: var(--cyan);
    padding: 42px 0 0 43px;
  }
  .values-box p {
    font-family: "Roboto Condensed", Arial, sans-serif; font-weight: 700;
    color: #ffffff; font-size: 30px; line-height: 41px;
  }

  .headline {
    left: 0; top: 598px; width: 420px; text-align: center;
    font-family: "Roboto Condensed", Arial, sans-serif; font-weight: 700;
    color: var(--headline-blue); font-size: 29px; line-height: 40px;
  }

  .benefits-band {
    left: 0; top: 706px; width: 800px; height: 320px;
    background: var(--navy-blue);
  }
  .benefit-list { list-style: none; color: #ffffff; font-size: 17px; line-height: 23px; }
  .benefit-list li { position: absolute; padding-left: 26px; }
  .benefit-list li svg { position: absolute; left: 0; top: 4px; width: 17px; height: 15px; }
  .col-left li { left: 13px; width: 390px; }
  .col-right li { left: 413px; width: 380px; }

  .contact {
    left: 44px; top: 1062px; color: var(--ink); font-size: 17px; line-height: 25px;
  }
  .call-line {
    left: 426px; top: 1052px;
    font-family: "Roboto Condensed", Arial, sans-serif; font-weight: 700;
    font-size: 27px; color: var(--headline-blue);
  }
  .call-line .phone { color: var(--cyan); }
  .website { left: 428px; top: 1088px; font-size: 22px; color: var(--ink); }
</style>
</head>
<body>
<main class="flyer">
  <div class="abs photo" role="img" aria-label="Photo of two smiling senior women hugging outdoors in warm sunlight"></div>

  <svg class="abs zigzag" style="top:0;height:48px" viewBox="0 0 800 48" aria-hidden="true">
    <defs>
      <pattern id="zig-top" width="40" height="48" patternUnits="userSpaceOnUse">
        <path d="M0 0 H40 V36 L20 16 L0 36 Z" fill="#ffffff"/>
        <path d="M0 36 L20 16 L40 36" fill="none" stroke="var(--navy-blue)" stroke-width="5"/>
      </pattern>
    </defs>
    <rect x="0" y="0" width="800" height="48" fill="url(#zig-top)"/>
  </svg>

  <div class="abs logo-box">
    <span class="logo-mark"></span>
    <span class="logo-name">Tamberlyn Funding Corp.</span>
  </div>

  <svg class="abs zigzag" style="top:500px;height:40px;width:425px" viewBox="0 0 425 40" aria-hidden="true">
    <defs>
      <pattern id="zig-photo" width="40" height="40" patternUnits="userSpaceOnUse">
        <path d="M0 32 L20 12 L40 32 V40 H0 Z" fill="#ffffff"/>
        <path d="M0 32 L20 12 L40 32" fill="none" stroke="var(--navy-blue)" stroke-width="5"/>
      </pattern>
    </defs>
    <rect x="0" y="0" width="425" height="40" fill="url(#zig-photo)"/>
  </svg>

  <div class="abs values-box">
    <p>Personal Attention</p>
    <p>Honesty, Integrity</p>
    <p>Resourcefulness</p>
    <p>Professionalism</p>
  </div>

  <h1 class="abs headline">IS AREVERSE MORTGAGE<br>RIGHT FOR YOU?</h1>

  <section class="abs benefits-band">
    <ul class="benefit-list col-left">
      <li style="top:54px"><svg viewBox="0 0 17 15"><path d="M1 8 L6 13 L16 1" fill="none" stroke="var(--tick-red)" stroke-width="3"/></svg>A Reverse mortgage is a specialized loan for seniors 62 and older allows seniors to access a portion of the equity in their home.</li>
      <li style="top:141px"><svg viewBox="0 0 17 15"><path d="M1 8 L6 13 L16 1" fill="none" stroke="var(--tick-red)" stroke-width="3"/></svg>No Celebrity Endorsers or talking heads here</li>
      <li style="top:183px"><svg viewBox="0 0 17 15"><path d="M1 8 L6 13 L16 1" fill="none" stroke="var(--tick-red)" stroke-width="3"/></svg>Solutions for seniors... Stop worrying Start</li>
      <li style="top:218px"><svg viewBox="0 0 17 15"><path d="M1 8 L6 13 L16 1" fill="none" stroke="var(--tick-red)" stroke-width="3"/></svg>Living Say Goodby to monthly payments with a reverse mortgage</li>
    </ul>
    <ul class="benefit-list col-right">
      <li style="top:54px"><svg viewBox="0 0 17 15"><path d="M1 8 L6 13 L16 1" fill="none" stroke="var(--tick-red)" stroke-width="3"/></svg>Secure Your Retirement With Us</li>
      <li style="top:86px"><svg viewBox="0 0 17 15"><path d="M1 8 L6 13 L16 1" fill="none" stroke="var(--tick-red)" stroke-width="3"/></svg>GKP Goverment Insured</li>
      <li style="top:118px"><svg viewBox="0 0 17 15"><path d="M1 8 L6 13 L16 1" fill="none" stroke="var(--tick-red)" stroke-width="3"/></svg>Retain Complete ownership of your Home</li>
      <li style="top:150px"><svg viewBox="0 0 17 15"><path d="M1 8 L6 13 L16 1" fill="none" stroke="var(--tick-red)" stroke-width="3"/></svg>Save and Effective Financial Tool</li>
      <li style="top:183px;line-height:30px"><svg viewBox="0 0 17 15"><path d="M1 8 L6 13 L16 1" fill="none" stroke="var(--tick-red)" stroke-width="3"/></svg>Pay Off Credit cards Elimanate Mortgage payments improve your home or lifestyle</li>
      <li style="top:247px"><svg viewBox="0 0 17 15"><path d="M1 8 L6 13 L16 1" fill="none" stroke="var(--tick-red)" stroke-width="3"/></svg>No Credit score or income requirements</li>
    </ul>
  </section>

  <svg class="abs zigzag" style="top:1000px;height:40px" viewBox="0 0 800 40" aria-hidden="true">
    <defs>
      <pattern id="zig-band" width="40" height="40" patternUnits="userSpaceOnUse">
        <path d="M0 32 L20 12 L40 32 V40 H0 Z" fill="#ffffff"/>
        <path d="M0 32 L20 12 L40 32" fill="none" stroke="var(--cyan)" stroke-width="5"/>
      </pattern>
    </defs>
    <rect x="0" y="0" width="800" height="40" fill="url(#zig-band)"/>
  </svg>

  <address class="abs contact" style="font-style:normal">
    Contact: Mr. Daniel Whitcombe<br>
    41 Harbor Ln. Suite 210, Millbrook, NY 12545
  </address>
  <p class="abs call-line">Call Us Today <span class="phone">(877) 520-6184</span></p>
  <p class="abs website">www.tamberlynfundingcorp.com</p>
</main>
</body>
</html>
```